Peeled Garlic Company needs a flyer design

Willow Acre is a factory that peeled garlic, pack them in plastic bags, and sells them to other businesses like restaurants and supermarkets. We are looking for a flyer that speaks health, nature, rustic, and professionalism

```html
<!DOCTYPE html>
<html lang="en">
<head>
<meta charset="UTF-8">
<title>Willow Acre – Peeled Garlic Flyer</title>
<link href="https://fonts.googleapis.com/css2?family=Montserrat:wght@700;800&family=Open+Sans:wght@400;600;700&display=swap" rel="stylesheet">
<style>
  :root{
    --stage:#242424;
    --green:#15893f;
    --headline-green:#178a3e;
    --lime:#c5d52d;
    --maroon:#5e1320;
    --orange:#ee8c22;
    --white:#ffffff;
    --ink:#1f1f1f;
  }
  html,body{margin:0;padding:0;width:1200px;height:1200px;overflow:hidden;background:var(--stage);}
  .flyer{position:absolute;left:136px;top:0;width:928px;height:1200px;background:var(--white);overflow:hidden;font-family:"Open Sans",sans-serif;}
  .hero-photo{position:absolute;left:0;top:0;width:928px;height:787px;
    background:linear-gradient(180deg,#8fb8dc 0%,#cfe1ee 22%,#f4f6f2 38%,#c9d89a 52%,#7f9a3f 62%,#a9b86a 72%,#6e4a33 80%,#5a3a27 100%);}
  .brand{position:absolute;left:60px;top:150px;display:flex;align-items:center;gap:14px;}
  .brand-dot{width:30px;height:30px;border-radius:50%;background:var(--maroon);}
  .brand-name{font-family:"Montserrat",sans-serif;font-weight:800;font-size:44px;color:var(--maroon);letter-spacing:1px;}
  .headline{position:absolute;left:410px;top:44px;margin:0;font-family:"Montserrat",sans-serif;font-weight:800;font-size:79px;line-height:80px;color:var(--headline-green);letter-spacing:-1px;}
  .subhead{position:absolute;left:413px;top:211px;width:460px;height:44px;background:var(--maroon);color:var(--white);font-family:"Montserrat",sans-serif;font-weight:700;font-size:25px;line-height:44px;text-align:center;}
  .capacity{position:absolute;left:0;top:718px;width:555px;height:69px;background:var(--orange);clip-path:polygon(0 0,505px 0,555px 69px,0 69px);}
  .capacity p{margin:0;padding:14px 0 0 54px;color:var(--white);font-weight:700;font-size:15.5px;line-height:20px;text-transform:uppercase;letter-spacing:.2px;}
  .benefits{position:absolute;left:0;top:787px;width:928px;height:280px;background:var(--green);display:flex;padding:0 28px;box-sizing:border-box;}
  .benefit{flex:1;text-align:center;padding-top:30px;position:relative;}
  .benefit + .benefit::before{content:"";position:absolute;left:0;top:36px;bottom:36px;border-left:1px solid rgba(197,213,45,.55);}
  .benefit-icon{width:82px;height:82px;border-radius:50%;background:var(--lime);margin:0 auto;display:flex;align-items:center;justify-content:center;}
  .benefit h3{margin:20px 0 6px;color:var(--lime);font-family:"Montserrat",sans-serif;font-weight:700;font-size:18px;}
  .benefit p{margin:0 auto;width:170px;color:var(--white);font-size:14.5px;line-height:18px;}
  .footer-note{position:absolute;left:55px;top:1100px;margin:0;color:var(--ink);font-size:14.5px;line-height:18px;width:410px;}
  .contact-panel{position:absolute;left:0;top:1067px;width:928px;height:133px;}
  .contact{position:absolute;right:55px;top:1100px;text-align:right;color:var(--ink);font-size:14.5px;line-height:18px;}
  .contact .web{font-weight:700;}
  .contact svg{vertical-align:-1px;}
</style>
</head>
<body>
<main class="flyer">
  <div class="hero-photo" role="img" aria-label="Photo of a sunny garlic field with a farm worker, bags of peeled garlic, garlic bulbs and a wooden bowl on a rustic wooden table"></div>

  <div class="brand"><span class="brand-dot"></span><span class="brand-name">Willow Acre</span></div>

  <h1 class="headline">FRESH AND<br>FLAVORFUL</h1>
  <div class="subhead">Peeled Garlic and Garlic Bulbs</div>

  <div class="capacity"><p>Willow Acre’s state-of-the-art equipment allow<br>us to produce 25 tons of peeled garlic per day</p></div>

  <section class="benefits">
    <div class="benefit">
      <div class="benefit-icon">
        <svg width="52" height="36" viewBox="0 0 52 36"><rect x="0" y="0" width="52" height="36" fill="#fff"/><rect x="0" y="0" width="22" height="18" fill="#c5d52d"/><g fill="#c5d52d"><rect x="22" y="4" width="30" height="3"/><rect x="22" y="11" width="30" height="3"/><rect x="0" y="22" width="52" height="3"/><rect x="0" y="29" width="52" height="3"/></g></svg>
      </div>
      <h3>Peeled in USA</h3>
      <p>Our garlic is peeled in USA, fresher and healthier than peeled garlic shipped from across the world</p>
    </div>
    <div class="benefit">
      <div class="benefit-icon">
        <svg width="44" height="48" viewBox="0 0 44 48"><path d="M22 2 C24 12 40 20 40 32 C40 42 32 46 22 46 C12 46 4 42 4 32 C4 20 20 12 22 2Z" fill="#fff"/><path d="M22 14 V44 M15 24 C12 32 14 40 18 44 M29 24 C32 32 30 40 26 44" stroke="#c5d52d" stroke-width="2" fill="none"/></svg>
      </div>
      <h3>More Flavor</h3>
      <p>We source the best garlic from all over the world so our peeled garlic is always fresh and in season</p>
    </div>
    <div class="benefit">
      <div class="benefit-icon">
        <svg width="48" height="44" viewBox="0 0 48 44"><path d="M22 42 C6 38 2 22 6 8 C18 12 26 24 22 42Z" fill="#fff"/><path d="M26 42 C26 24 32 10 46 4 C48 22 40 38 26 42Z" fill="#fff"/></svg>
      </div>
      <h3>No Preservatives</h3>
      <p>We use no preservatives, unlike products that are shipped from across the world</p>
    </div>
    <div class="benefit">
      <div class="benefit-icon">
        <svg width="42" height="48" viewBox="0 0 42 48"><path d="M21 2 L39 9 V23 C39 35 31 42 21 46 C11 42 3 35 3 23 V9Z" fill="none" stroke="#fff" stroke-width="3.5"/><path d="M13 24 L19 30 L30 17" fill="none" stroke="#fff" stroke-width="4" stroke-linecap="round" stroke-linejoin="round"/></svg>
      </div>
      <h3>Safe and Reliable</h3>
      <p>We are GMP, HACCP, and PADA certified and follows the highest food safety standards.</p>
    </div>
  </section>

  <svg class="contact-panel" viewBox="0 0 928 133" aria-hidden="true"><polygon points="430,0 928,0 928,133 515,133" fill="var(--lime)"/></svg>

  <p class="footer-note">Peeling garlic in the US allows us to scale up and down quickly to satisfy our customer’s demands, since we don’t have to wait for shipping from overseas.</p>

  <address class="contact" style="font-style:normal">
    18 Cedar Hollow Lane, Millbrook, Ohio, USA.<br>
    <svg width="10" height="13" viewBox="0 0 10 13"><path d="M2 1 L4 1 L5 4 L3.5 5 C4 7 5 8.5 6.5 9.5 L7.5 8 L10 9.5 L9.5 12 C5 12 1 7 1 2Z" fill="var(--headline-green)"/></svg> +1-555-014-2290 &nbsp;|&nbsp;
    <svg width="13" height="10" viewBox="0 0 13 10"><rect x="0" y="0" width="13" height="10" fill="var(--headline-green)"/><path d="M0 0 L6.5 5.5 L13 0" stroke="#fff" stroke-width="1.2" fill="none"/></svg> hello@willowacrefarm.com<br>
    <span class="web">www.willowacrefarm.com</span>
  </address>
</main>
</body>
</html>
```